Vellmar Detailing – Premium Automotive Detailing Studio Website Design

We're launching a premium automotive detailing studio called Vellmar Detailing, and we’re looking for a clean, minimal, and high-end website design (desktop + mobile version). The studio targets owners of luxury vehicles who care deeply about aesthetics, perfection, and exceptional service.
This project is about more than just showing services , it should feel like a luxury experience from the very first second. The design should be modern, minimalistic, elegant, and clearly aimed at an upscale market.
We’re looking for a designer who can translate our physical studio’s premium interior and architectural feel into a digital presence.
What we want the website to feel like:
Clean and modern
Professional and luxurious
Minimal and not cluttered
Light animations or transitions to add polish
Stylish and cinematic
Design freedom:
We trust your design direction. We are not providing strict color codes or layout instructions, we want you to create what you believe works best based on our brand positioning and target audience. Just keep it premium, modern, and well-organized.
What the website should include:
Hero section with a bold visual (image or video)
About the Studio — a few blocks explaining our story and focus on quality
Service Overview — clearly showing what we offer (detailing, ceramic coating, interior, etc.)
Gallery/Showcase — show off our work with cars, interior, and the space itself
Client Lounge Area — mention comfort, coffee, and waiting space
Testimonials — social proof from satisfied clients
Location & contact section — map, address, contact form
Footer, simple with nav, contact info, and optional social media
Target audience:
Owners of high-end vehicles (Torvani, Kellard, etc.)
Car collectors and detailing enthusiasts
People looking for premium-level service and presentation
Brands/creators booking our photo studio

```html
<!DOCTYPE html>
<html lang="en">
<head>
<meta charset="utf-8">
<title>Vellmar Detailing – Premium Automotive Detailing Studio</title>
<link href="https://fonts.googleapis.com/css2?family=Exo+2:wght@600;700&family=Inter:wght@400;500;600;700&display=swap" rel="stylesheet">
<style>
:root{
  --red:#d3291f;
  --ink:#141414;
  --dark:#1c1c1c;
  --panel:#2a2a2a;
  --light:#e4e4e4;
  --paper:#ffffff;
  --muted:#b9b9b9;
  --line:#3a3a3a;
  --star:#f4b400;
}
*{box-sizing:border-box;margin:0;padding:0}
html,body{width:1200px;height:5098px;overflow:hidden}
body{font-family:"Inter",sans-serif;color:var(--paper);background:var(--ink);position:relative}
.band{position:absolute;left:0;width:1200px;overflow:hidden}
.heading{font-family:"Exo 2",sans-serif;font-weight:700;text-transform:uppercase;letter-spacing:1px;line-height:1.25}
.eyebrow{font-size:11px;font-weight:700;letter-spacing:1.5px;text-transform:uppercase}
.btn{position:absolute;background:var(--red);color:#fff;font-size:12px;font-weight:700;text-transform:uppercase;display:flex;align-items:center;justify-content:center;gap:7px;letter-spacing:.3px}
.btn svg{width:12px;height:12px}
.photo{position:absolute}
.brand{display:flex;align-items:center;gap:9px;color:#fff;font-family:"Exo 2",sans-serif;font-weight:700;text-transform:uppercase;line-height:1}
.brand .mark{width:20px;height:20px;background:#fff}
.brand .name{display:flex;flex-direction:column;gap:2px}
.brand .name span:first-child{font-size:21px;letter-spacing:1px}
.brand .name span:last-child{font-size:12px;letter-spacing:6px}
.social{display:flex;gap:22px}
.social i{display:block;width:10px;height:10px;border-radius:50%;background:#fff}

/* Hero */
.hero{top:0;height:657px;background:linear-gradient(110deg,#3a3d44 0%,#24262c 35%,#1b2a55 62%,#0f1d4a 100%)}
.hero-photo{position:absolute;inset:0}
.hero-shade{position:absolute;inset:0;background:linear-gradient(90deg,rgba(0,0,0,.15),rgba(0,0,0,.45) 60%,rgba(0,0,0,.3))}
.topbar{position:absolute;top:0;left:0;width:1200px;height:44px;background:rgba(20,20,20,.85);font-size:11px}
.topbar .social{position:absolute;left:85px;top:17px}
.topbar-contact{position:absolute;right:85px;top:15px;display:flex;gap:28px}
.topbar-contact span{display:flex;align-items:center;gap:6px}
.nav{position:absolute;top:66px;left:85px;width:1030px;height:44px}
.nav .brand{position:absolute;left:0;top:6px}
.nav-links{position:absolute;left:220px;top:13px;display:flex;gap:28px;list-style:none;font-size:14px}
.nav-links li:first-child{border-bottom:2px solid var(--red);padding-bottom:2px}
.nav-cta{right:0;top:0;width:167px;height:44px}
.hero-eyebrow{position:absolute;left:620px;top:272px;letter-spacing:5px}
.hero-title{position:absolute;left:620px;top:288px;font-size:50px}
.hero-text{position:absolute;left:620px;top:364px;width:440px;font-size:15px;line-height:1.6}
.hero-cta{left:620px;top:443px;width:152px;height:44px}
.counter{position:absolute;left:1098px;top:276px;font-size:18px;font-family:"Exo 2",sans-serif}
.counter .bar{position:absolute;left:10px;top:34px;width:1px;height:120px;background:rgba(255,255,255,.5)}
.counter .end{position:absolute;top:180px;left:2px;font-size:11px;font-weight:700}

/* About */
.about{top:657px;height:586px;background:var(--ink)}
.about-p1{left:85px;top:109px;width:235px;height:322px;background:linear-gradient(160deg,#cfcfcf,#6d6d6d 55%,#3a3a3a)}
.about-p2{left:342px;top:173px;width:235px;height:320px;background:linear-gradient(150deg,#2a2a2a,#b5151b 45%,#5b0c0f)}
.about-eyebrow{position:absolute;left:635px;top:151px}
.about-title{position:absolute;left:635px;top:172px;font-size:40px;width:470px}
.about-text{position:absolute;left:635px;top:285px;width:440px;font-size:13px;line-height:1.85;color:#e6e6e6}
.about-cta{left:635px;top:436px;width:155px;height:45px}

/* Cards */
.card{position:absolute;overflow:hidden}
.card-fade{position:absolute;inset:0;background:linear-gradient(180deg,rgba(0,0,0,0) 50%,rgba(0,0,0,.7))}
.card-cap{position:absolute;left:15px;right:15px;bottom:20px;color:#fff}
.card-cap h3{font-family:"Exo 2",sans-serif;font-weight:700;font-size:17px;text-transform:uppercase;letter-spacing:.5px}
.card-cap p{font-size:13px;line-height:1.5;width:185px;margin-top:4px}
.card-more{position:absolute;right:15px;bottom:30px;font-size:12px;font-weight:700;display:flex;gap:6px;align-items:center;border-bottom:1px solid #fff;padding-bottom:2px;text-transform:uppercase;color:#fff}
.card-more svg{width:12px;height:12px}

/* Services */
.services{top:1243px;height:702px;background:var(--light);color:var(--ink)}
.services-eyebrow{position:absolute;left:85px;top:77px}
.services-title{position:absolute;left:85px;top:97px;font-size:38px;width:760px}
.service-card{top:237px;width:323px;height:375px}
.s1{left:85px;background:linear-gradient(160deg,#d8d8d8,#4a5575 50%,#1b2a6b)}
.s2{left:438px;background:linear-gradient(150deg,#1f1f1f,#c0202a 55%,#3b3b3b)}
.s3{left:792px;background:linear-gradient(140deg,#7a8a9a,#dedede 45%,#4b4b4b)}

/* Gallery */
.gallery{top:1945px;height:667px;background:var(--dark);text-align:center}
.gallery-eyebrow{position:absolute;left:0;right:0;top:71px}
.gallery-title{position:absolute;left:0;right:0;top:91px;font-size:38px}
.g1{left:115px;top:245px;width:130px;height:242px;background:linear-gradient(150deg,#d7d7d7,#555)}
.g2{left:245px;top:205px;width:193px;height:322px;background:linear-gradient(150deg,#e2e2e2,#444 55%,#d9c81c 80%)}
.g3{left:438px;top:165px;width:324px;height:402px;background:linear-gradient(160deg,#9a9a9a,#3d3d3d 60%,#222)}
.g4{left:762px;top:205px;width:193px;height:322px;background:linear-gradient(150deg,#dcdcdc,#7db7e6 50%,#2d2d2d)}
.g5{left:955px;top:245px;width:130px;height:242px;background:linear-gradient(150deg,#e8e8e8,#222 70%)}
.arrow{position:absolute;top:597px;width:36px;height:36px;border-radius:50%;display:flex;align-items:center;justify-content:center}
.arrow.prev{left:557px;border:1px solid #fff}
.arrow.next{left:605px;background:var(--red)}
.arrow svg{width:16px;height:16px}

/* Lounge */
.lounge{top:2612px;height:633px;background:var(--paper);color:var(--ink)}
.lounge-eyebrow{position:absolute;left:85px;top:88px}
.lounge-title{position:absolute;left:85px;top:107px;font-size:38px}
.lounge-intro{position:absolute;left:612px;top:45px;width:505px;font-size:13px;line-height:1.85;color:#444}
.lounge-cta{left:612px;top:138px;width:155px;height:43px}
.lounge-card{top:218px;width:331px;height:328px}
.lounge-card .card-cap p{width:290px}
.l1{left:85px;background:linear-gradient(150deg,#e9ecef,#8fa2c4 45%,#4d5c78)}
.l2{left:434px;background:linear-gradient(150deg,#d2d2d2,#8a5f4f 50%,#3d3d3d)}
.l3{left:784px;background:linear-gradient(150deg,#f1f1f1,#a9a9a9 50%,#5a5a5a)}

/* Reviews */
.reviews{top:3245px;height:650px;background:var(--ink)}
.reviews-rule{position:absolute;left:85px;top:60px;width:55px;height:2px;background:var(--red)}
.reviews-eyebrow{position:absolute;left:85px;top:73px;letter-spacing:6px}
.reviews-title{position:absolute;left:85px;top:92px;font-size:38px}
.rating{position:absolute;left:85px;top:153px;display:flex;align-items:center;gap:12px;font-size:11px}
.rating-word{font-weight:500;font-size:27px;color:#fff}
.stars{display:flex;gap:3px}
.stars svg{width:11px;height:11px;fill:var(--star)}
.review{position:absolute;top:217px;width:331px;height:341px;background:var(--panel);padding:28px 20px}
.review .stars svg{width:14px;height:14px}
.review-badge{position:absolute;right:24px;top:28px;width:20px;height:20px;border-radius:50%;border:3px solid #fff}
.review-text{margin-top:20px;font-size:13px;line-height:1.85;color:#e0e0e0}
.review-name{position:absolute;left:20px;top:278px;font-size:16px;font-weight:600}
.review-role{position:absolute;left:20px;top:303px;font-size:11px;color:var(--muted)}

/* Contact */
.contact-sec{top:3895px;height:661px;background:var(--light);color:#fff}
.map{position:absolute;left:158px;top:120px;width:497px;height:410px;background:linear-gradient(135deg,#f2f2f2,#dde8dd 55%,#cfe0cf)}
.form{position:absolute;left:655px;top:60px;width:390px;height:520px;background:#2b2b2b}
.form-eyebrow{position:absolute;left:32px;top:51px}
.form-title{position:absolute;left:32px;top:68px;font-size:37px}
.field{position:absolute;left:35px;width:320px;height:42px;border:1px solid #8a8a8a;border-radius:21px;font-size:12px;padding:13px 18px;display:flex;justify-content:space-between}
.field.msg{height:92px;border-radius:12px}
.form-submit{left:35px;top:460px;width:320px;height:43px}

/* Footer */
.footer{top:4556px;height:542px;background:var(--ink)}
.footer-title{position:absolute;left:83px;top:55px;font-size:36px}
.totop{position:absolute;right:85px;top:76px;font-size:11px;font-weight:700;display:flex;gap:6px;align-items:center}
.hline{position:absolute;left:85px;width:1030px;height:1px;background:var(--line)}
.vline{position:absolute;left:373px;top:134px;width:1px;height:354px;background:var(--line)}
.footer .brand{position:absolute;left:133px;top:252px}
.col{position:absolute;top:212px;font-size:13px}
.col h5{font-family:"Exo 2",sans-serif;font-size:16px;text-transform:uppercase;letter-spacing:.5px;margin-bottom:14px}
.col .row{display:flex;gap:10px;line-height:1.75;color:#dcdcdc}
.col .row svg{width:13px;height:13px;margin-top:5px;flex:none}
.col ul{list-style:none;color:#dcdcdc;line-height:2.05}
.copy{position:absolute;left:85px;top:505px;font-size:10px;letter-spacing:1px;color:var(--muted)}
.copy b{color:#fff}
.date{position:absolute;right:85px;top:505px;font-size:10px;letter-spacing:1px;color:var(--muted)}
</style>
</head>
<body>

<header class="band hero">
  <div class="hero-photo" role="img" aria-label="Detailer in a face mask machine-polishing a dark blue luxury car in a dim studio"></div>
  <div class="hero-shade"></div>
  <div class="topbar">
    <div class="social" aria-label="Social links"><i></i><i></i><i></i><i></i></div>
    <div class="topbar-contact">
      <span><svg width="12" height="12" viewBox="0 0 24 24" fill="none" stroke="#fff" stroke-width="2"><path d="M5 3h4l2 5-3 2a11 11 0 0 0 6 6l2-3 5 2v4a2 2 0 0 1-2 2A17 17 0 0 1 3 5a2 2 0 0 1 2-2z"/></svg>Call Us: 1800 555 014</span>
      <span><svg width="12" height="12" viewBox="0 0 24 24" fill="none" stroke="#fff" stroke-width="2"><rect x="3" y="5" width="18" height="14"/><path d="M3 6l9 7 9-7"/></svg>Message us: support@vellmardetailing.com</span>
    </div>
  </div>
  <nav class="nav">
    <div class="brand"><span class="mark"></span><span class="name"><span>Vellmar</span><span>Detailing</span></span></div>
    <ul class="nav-links"><li>Home</li><li>About</li><li>Services</li><li>Gallery</li><li>Client Lounge</li><li>Testimonials</li><li>Contact Us</li></ul>
    <div class="btn nav-cta">Make Appointment</div>
  </nav>
  <div class="eyebrow hero-eyebrow">Premium Automotive</div>
  <h1 class="heading hero-title">Detailing Studio</h1>
  <p class="hero-text">Morbi erat quam, aliquet ut eleifend pretium, scelerisque at velit. Etiam facilisis cursus pellentesque</p>
  <div class="btn hero-cta"><svg viewBox="0 0 24 24" fill="none" stroke="#fff" stroke-width="2.5"><path d="M5 12h14M13 6l6 6-6 6"/></svg>Read More</div>
  <div class="counter">01<span class="bar"></span><span class="end">04</span></div>
</header>

<section class="band about">
  <div class="photo about-p1" role="img" aria-label="Detailer in an apron wiping a car surface"></div>
  <div class="photo about-p2" role="img" aria-label="Polisher buffing the headlight area of a red car"></div>
  <div class="eyebrow about-eyebrow">About Us</div>
  <h2 class="heading about-title">Restoring Lasting Shine, Inside and Out</h2>
  <p class="about-text">Cras fermentum lectus nec elit tincidunt semper. Mauris ac diam at tellus mattis rhoncus vitae eu mi. Etiam rhoncus erat vitae semper facilisis. Aenean eu posuere lorem. Vivamus aliquam tellus velit. Donec ornare, tortor eu pa ultrices, lorem est suscipit ex, a euismod lacus lectus ut quam.</p>
  <div class="btn about-cta"><svg viewBox="0 0 24 24" fill="none" stroke="#fff" stroke-width="2.5"><path d="M5 12h14M13 6l6 6-6 6"/></svg>Read More</div>
</section>

<section class="band services">
  <div class="eyebrow services-eyebrow">Services</div>
  <h2 class="heading services-title">Vellmar Detailing Services That Go Beyond Expectations</h2>
  <article class="card service-card s1" role="img" aria-label="Technician polishing the paint of a blue car in a garage">
    <div class="card-fade"></div>
    <div class="card-cap"><h3>Detailing</h3><p>Vivamus aliquam tellus velit. Donec ornare, tortor</p></div>
    <div class="card-more"><svg viewBox="0 0 24 24" fill="none" stroke="#fff" stroke-width="2.5"><path d="M5 12h14M13 6l6 6-6 6"/></svg>Read More</div>
  </article>
  <article class="card service-card s2" role="img" aria-label="Gloved hand applying ceramic coating to a red car">
    <div class="card-fade"></div>
    <div class="card-cap"><h3>Ceramic Coating</h3><p>Vivamus aliquam tellus velit. Donec ornare, tortor</p></div>
    <div class="card-more"><svg viewBox="0 0 24 24" fill="none" stroke="#fff" stroke-width="2.5"><path d="M5 12h14M13 6l6 6-6 6"/></svg>Read More</div>
  </article>
  <article class="card service-card s3" role="img" aria-label="Consultant seated beside paint swatches and a white car">
    <div class="card-fade"></div>
    <div class="card-cap"><h3>Interior</h3><p>Vivamus aliquam tellus velit. Donec ornare, tortor</p></div>
    <div class="card-more"><svg viewBox="0 0 24 24" fill="none" stroke="#fff" stroke-width="2.5"><path d="M5 12h14M13 6l6 6-6 6"/></svg>Read More</div>
  </article>
</section>

<section class="band gallery">
  <div class="eyebrow gallery-eyebrow">Gallery</div>
  <h2 class="heading gallery-title">View Our Work</h2>
  <div class="photo g1" role="img" aria-label="Detailer polishing a car bonnet"></div>
  <div class="photo g2" role="img" aria-label="Yellow polishing pad on a machine buffer"></div>
  <div class="photo g3" role="img" aria-label="Detailer cleaning the front of a grey car"></div>
  <div class="photo g4" role="img" aria-label="Gloved hands waxing a car headlight"></div>
  <div class="photo g5" role="img" aria-label="Detailer buffing a white car"></div>
  <div class="arrow prev"><svg viewBox="0 0 24 24" fill="none" stroke="#fff" stroke-width="2"><path d="M19 12H5M11 6l-6 6 6 6"/></svg></div>
  <div class="arrow next"><svg viewBox="0 0 24 24" fill="none" stroke="#fff" stroke-width="2"><path d="M5 12h14M13 6l6 6-6 6"/></svg></div>
</section>

<section class="band lounge">
  <div class="eyebrow lounge-eyebrow">Lounge Area</div>
  <h2 class="heading lounge-title">Client Lounge Area</h2>
  <p class="lounge-intro">Vivamus facilisis vel lacus id iaculis. Etiam faucibus finibus interdum. Etiam ex tortor, aliquam et suscipit in, vulputate id justo. Phasellus a quam id erat pulvinar finibus ac non elit.</p>
  <div class="btn lounge-cta"><svg viewBox="0 0 24 24" fill="none" stroke="#fff" stroke-width="2.5"><path d="M5 12h14M13 6l6 6-6 6"/></svg>Read More</div>
  <article class="card lounge-card l1" role="img" aria-label="Client relaxing in a lounge chair">
    <div class="card-fade"></div>
    <div class="card-cap"><h3>Comfort Zone</h3><p>Vivamus aliquam tellus velit. Donec ornare, tortor eu pa ultrices,</p></div>
  </article>
  <article class="card lounge-card l2" role="img" aria-label="Two clients chatting over coffee in the studio">
    <div class="card-fade"></div>
    <div class="card-cap"><h3>Coffee Area</h3><p>Vivamus aliquam tellus velit. Donec ornare, tortor eu pa ultrices,</p></div>
  </article>
  <article class="card lounge-card l3" role="img" aria-label="Client seated in a bright waiting room">
    <div class="card-fade"></div>
    <div class="card-cap"><h3>Waiting Space</h3><p>Vivamus aliquam tellus velit. Donec ornare, tortor eu pa ultrices,</p></div>
  </article>
</section>

<section class="band reviews">
  <div class="reviews-rule"></div>
  <div class="eyebrow reviews-eyebrow">Testimonials</div>
  <h2 class="heading reviews-title">Our Revora Reviews</h2>
  <div class="rating">
    <span class="rating-word">Revora</span>
    <span class="stars"><svg viewBox="0 0 24 24"><path d="M12 2l3 7h7l-6 4 2 8-6-5-6 5 2-8-6-4h7z"/></svg><svg viewBox="0 0 24 24"><path d="M12 2l3 7h7l-6 4 2 8-6-5-6 5 2-8-6-4h7z"/></svg><svg viewBox="0 0 24 24"><path d="M12 2l3 7h7l-6 4 2 8-6-5-6 5 2-8-6-4h7z"/></svg><svg viewBox="0 0 24 24"><path d="M12 2l3 7h7l-6 4 2 8-6-5-6 5 2-8-6-4h7z"/></svg><svg viewBox="0 0 24 24"><path d="M12 2l3 7h7l-6 4 2 8-6-5-6 5 2-8-6-4h7z"/></svg></span>
    <span>4.8 rating of 25,000</span>
  </div>
  <article class="review" style="left:85px">
    <div class="stars"><svg viewBox="0 0 24 24"><path d="M12 2l3 7h7l-6 4 2 8-6-5-6 5 2-8-6-4h7z"/></svg><svg viewBox="0 0 24 24"><path d="M12 2l3 7h7l-6 4 2 8-6-5-6 5 2-8-6-4h7z"/></svg><svg viewBox="0 0 24 24"><path d="M12 2l3 7h7l-6 4 2 8-6-5-6 5 2-8-6-4h7z"/></svg><svg viewBox="0 0 24 24"><path d="M12 2l3 7h7l-6 4 2 8-6-5-6 5 2-8-6-4h7z"/></svg><svg viewBox="0 0 24 24"><path d="M12 2l3 7h7l-6 4 2 8-6-5-6 5 2-8-6-4h7z"/></svg></div>
    <span class="review-badge"></span>
    <p class="review-text">Donec non ante at enim faucibus eleifend laoreet non dui. Phasellus at diam neque. Praesent sed elit felis. Nullaorta ullamcorper erat, in mattis ex lobortis ac. Sed ex urna, fermentum vitae sagittis ac, molestie quis sem. Sed in lobortis ipsum. Curabitur et mauris dapibus</p>
    <h4 class="review-name">Elias Marron</h4><small class="review-role">Customer</small>
  </article>
  <article class="review" style="left:434px">
    <div class="stars"><svg viewBox="0 0 24 24"><path d="M12 2l3 7h7l-6 4 2 8-6-5-6 5 2-8-6-4h7z"/></svg><svg viewBox="0 0 24 24"><path d="M12 2l3 7h7l-6 4 2 8-6-5-6 5 2-8-6-4h7z"/></svg><svg viewBox="0 0 24 24"><path d="M12 2l3 7h7l-6 4 2 8-6-5-6 5 2-8-6-4h7z"/></svg><svg viewBox="0 0 24 24"><path d="M12 2l3 7h7l-6 4 2 8-6-5-6 5 2-8-6-4h7z"/></svg><svg viewBox="0 0 24 24"><path d="M12 2l3 7h7l-6 4 2 8-6-5-6 5 2-8-6-4h7z"/></svg></div>
    <span class="review-badge"></span>
    <p class="review-text">Donec non ante at enim faucibus eleifend laoreet non dui. Phasellus at diam neque. Praesent sed elit felis. Nullaorta ullamcorper erat, in mattis ex lobortis ac. Sed ex urna, fermentum vitae sagittis ac, molestie quis sem. Sed in lobortis ipsum. Curabitur et mauris dapibus</p>
    <h4 class="review-name">Elias Marron</h4><small class="review-role">Customer</small>
  </article>
  <article class="review" style="left:784px">
    <div class="stars"><svg viewBox="0 0 24 24"><path d="M12 2l3 7h7l-6 4 2 8-6-5-6 5 2-8-6-4h7z"/></svg><svg viewBox="0 0 24 24"><path d="M12 2l3 7h7l-6 4 2 8-6-5-6 5 2-8-6-4h7z"/></svg><svg viewBox="0 0 24 24"><path d="M12 2l3 7h7l-6 4 2 8-6-5-6 5 2-8-6-4h7z"/></svg><svg viewBox="0 0 24 24"><path d="M12 2l3 7h7l-6 4 2 8-6-5-6 5 2-8-6-4h7z"/></svg><svg viewBox="0 0 24 24"><path d="M12 2l3 7h7l-6 4 2 8-6-5-6 5 2-8-6-4h7z"/></svg></div>
    <span class="review-badge"></span>
    <p class="review-text">Donec non ante at enim faucibus eleifend laoreet non dui. Phasellus at diam neque. Praesent sed elit felis. Nullaorta ullamcorper erat, in mattis ex lobortis ac. Sed ex urna, fermentum vitae sagittis ac, molestie quis sem. Sed in lobortis ipsum. Curabitur et mauris dapibus</p>
    <h4 class="review-name">Elias Marron</h4><small class="review-role">Customer</small>
  </article>
</section>

<section class="band contact-sec">
  <div class="map" role="img" aria-label="Street map showing the studio location and surrounding parks"></div>
  <div class="form">
    <div class="eyebrow form-eyebrow">Contact Us</div>
    <h2 class="heading form-title">Get In Touch</h2>
    <div class="field" style="top:130px">Name</div>
    <div class="field" style="top:182px">Email</div>
    <div class="field" style="top:234px">Phone</div>
    <div class="field" style="top:286px">Select Subject<svg width="10" height="10" viewBox="0 0 24 24" fill="none" stroke="#fff" stroke-width="2"><path d="M6 9l6 6 6-6"/></svg></div>
    <div class="field msg" style="top:338px">Message</div>
    <div class="btn form-submit"><svg viewBox="0 0 24 24" fill="none" stroke="#fff" stroke-width="2.5"><path d="M5 12h14M13 6l6 6-6 6"/></svg>Submit</div>
  </div>
</section>

<footer class="band footer">
  <h2 class="heading footer-title">Premium Automotive Detailing Studio</h2>
  <div class="totop">GO TO TOP <svg width="12" height="12" viewBox="0 0 24 24" fill="none" stroke="#fff" stroke-width="2"><path d="M12 19V5M6 11l6-6 6 6"/></svg></div>
  <div class="hline" style="top:134px"></div>
  <div class="vline"></div>
  <div class="brand"><span class="mark"></span><span class="name"><span>Vellmar</span><span>Detailing</span></span></div>
  <div class="col" style="left:447px">
    <h5>Address</h5>
    <div class="row"><svg viewBox="0 0 24 24" fill="none" stroke="#fff" stroke-width="2"><path d="M12 22s7-7 7-12a7 7 0 0 0-14 0c0 5 7 12 7 12z"/><circle cx="12" cy="10" r="2.5"/></svg><span>418 Harlow Lane Suite 200<br>Brenmoor</span></div>
    <h5 style="margin-top:26px">Contact Info</h5>
    <div class="row"><svg viewBox="0 0 24 24" fill="none" stroke="#fff" stroke-width="2"><path d="M5 3h4l2 5-3 2a11 11 0 0 0 6 6l2-3 5 2v4a2 2 0 0 1-2 2A17 17 0 0 1 3 5a2 2 0 0 1 2-2z"/></svg><span>1800 555 014</span></div>
    <div class="row"><svg viewBox="0 0 24 24" fill="none" stroke="#fff" stroke-width="2"><rect x="3" y="5" width="18" height="14"/><path d="M3 6l9 7 9-7"/></svg><span>support@vellmardetailing.com</span></div>
  </div>
  <div class="col" style="left:775px">
    <h5>Quick Links</h5>
    <ul><li>Home</li><li>About</li><li>Services</li><li>Gallery</li><li>Client Lounge</li><li>Testimonials</li><li>Contact Us</li></ul>
  </div>
  <div class="col" style="left:980px">
    <h5>Follow Us</h5>
    <div class="social" aria-label="Social links"><i></i><i></i><i></i><i></i></div>
  </div>
  <div class="hline" style="top:488px"></div>
  <div class="copy">© 2025 <b>VELLMAR DETAILING</b>. ALL RIGHT RESERVED.</div>
  <div class="date">JULY 30, 2025. LAYOUT_4</div>
</footer>

</body>
</html>
```